Business Card Design Project

I am community manager and social media strategist. I need a double sided business card with company logo and name. Looking for something professional, elegant but also a little bit original.

• - The logo and the colours are the company colours and a required to stay.
- The size should be: 84 x 55 mm (or 3.30 x 2.16)
- The file size should be: 1039 x 697 pixels (300 dpi)
- I'd like rounded corners. :)

Use the following contact information for the card:

Léonie Vardin
Stratégie médias sociaux / community management / édition de sites sociaux
mob. : 0687529103
leonie.vardin@postelune.fr
Twitter. : @lvardin
Skype : vardin.leonie

```html
<!DOCTYPE html>
<html lang="fr">
<head>
<meta charset="utf-8">
<title>Léonie Vardin — carte de visite</title>
<link rel="stylesheet" href="https://fonts.googleapis.com/css2?family=PT+Serif:wght@400;700&display=swap">
<style>
  :root {
    --page: #ffffff;
    --blue-deep: #2c558d;
    --blue-mid: #3a6aa5;
    --blue-light: #5a8cc4;
    --ink-blue: #2f5a92;
    --text-blue: #3b5f94;
    --rule: #9a9a9a;
    --card-edge: #b9b9b9;
    --white: #ffffff;
  }
  * { box-sizing: border-box; margin: 0; padding: 0; }
  html, body {
    width: 1200px; height: 900px; overflow: hidden;
    background: var(--page);
    font-family: "PT Serif", Georgia, serif;
  }
  .canvas { position: relative; width: 1200px; height: 900px; }

  .card {
    position: absolute; left: 280px; width: 636px;
    border-radius: 36px; overflow: hidden;
  }
  .card--front {
    top: 36px; height: 416px;
    background: linear-gradient(120deg, var(--blue-light) 0%, var(--blue-mid) 38%, var(--blue-deep) 100%);
  }
  .card--front .sheen { position: absolute; inset: 0; }
  .brand-mark {
    position: absolute; left: 130px; top: 120px;
    display: flex; align-items: center; gap: 14px;
    color: var(--white); font-weight: 700; font-size: 30px; letter-spacing: 1px;
    white-space: nowrap;
  }
  .brand-mark .dot {
    width: 22px; height: 22px; border-radius: 50%; background: var(--white);
  }
  .holder-name {
    position: absolute; left: 384px; top: 330px;
    color: var(--white); font-size: 28px; font-weight: 400;
    white-space: nowrap;
  }

  .card--back {
    top: 452px; height: 414px;
    background: var(--white);
    border: 2px solid var(--card-edge);
  }
  .company {
    position: absolute; left: 112px; top: 226px;
    display: flex; align-items: center; gap: 10px;
    color: var(--ink-blue); font-weight: 700; font-size: 26px; letter-spacing: 1px;
    white-space: nowrap;
  }
  .company .dot { width: 16px; height: 16px; border-radius: 50%; background: var(--ink-blue); }
  .divider {
    position: absolute; left: 318px; top: 130px;
    width: 2px; height: 146px; background: var(--rule);
  }
  .contact {
    position: absolute; left: 376px; top: 158px;
    list-style: none; color: var(--text-blue);
    font-size: 15px; line-height: 24px; white-space: nowrap;
  }
  .services {
    position: absolute; left: 0; right: 0; top: 338px;
    display: flex; justify-content: center;
    color: var(--text-blue); font-size: 15px; line-height: 20px;
    white-space: nowrap;
  }
  .services span { padding: 0 6px; }
  .services span + span { border-left: 2px solid var(--text-blue); }
</style>
</head>
<body>
<main class="canvas">
  <section class="card card--front" aria-label="Recto">
    <svg class="sheen" width="636" height="416" viewBox="0 0 636 416" aria-hidden="true">
      <path d="M0 140 C 180 150, 360 220, 636 300 L 636 250 C 380 170, 200 110, 0 110 Z" fill="#ffffff" opacity="0.08"/>
    </svg>
    <div class="brand-mark"><span class="dot"></span>ORVALIA</div>
    <p class="holder-name">Léonie Vardin</p>
  </section>

  <section class="card card--back" aria-label="Verso">
    <div class="company"><span class="dot"></span>ORVALIA</div>
    <div class="divider"></div>
    <ul class="contact">
      <li>Mob. : 0687529103</li>
      <li>leonie.vardin@postelune.fr</li>
      <li>Twitter. : @lvardin</li>
      <li>Skype : vardin.leonie</li>
    </ul>
    <p class="services">
      <span>Stratégie Médias Sociaux</span><span>Community Management</span><span>Édition De Sites Sociaux</span>
    </p>
  </section>
</main>
</body>
</html>
```